Business card for home developer

Name, email, phone #, logo, address, lic # and slogan.
Slogan to say something like, "Setting the Standard for Community Living" maybe? The last one said "A sept above the rest". Some thing saying we are above the other people.
The card can be two sided?
Home buyers
Business

```html
<!DOCTYPE html>
<html lang="en">
<head>
<meta charset="utf-8">
<title>Ridgeline Homes – Business Card</title>
<link rel="stylesheet" href="https://fonts.googleapis.com/css2?family=Lato:ital,wght@0,400;0,700;0,900;1,400&display=swap">
<style>
  :root {
    --page-bg: #e9e9e9;
    --card-white: #ffffff;
    --brand-blue: #1f3f86;
    --brand-red: #b8262b;
    --text-light: #ffffff;
    --text-soft: #e6ebf5;
  }

  * { box-sizing: border-box; margin: 0; padding: 0; }

  html, body {
    width: 1200px;
    height: 900px;
    overflow: hidden;
  }

  body {
    background: var(--page-bg);
    font-family: "Lato", sans-serif;
    display: flex;
    align-items: center;
    justify-content: center;
  }

  .business-card {
    width: 1000px;
    height: 572px;
    background: var(--card-white);
    display: flex;
    flex-direction: column;
    overflow: hidden;
  }

  .card-brand {
    height: 232px;
    display: flex;
    align-items: center;
    justify-content: center;
    gap: 20px;
  }

  .brand-name {
    font-weight: 900;
    font-size: 64px;
    letter-spacing: 1px;
    color: var(--brand-blue);
    text-transform: uppercase;
    line-height: 1;
  }

  .brand-mark {
    width: 56px;
    height: 56px;
  }

  .card-slogan {
    height: 42px;
    background: var(--brand-red);
    color: var(--text-light);
    display: flex;
    align-items: center;
    justify-content: center;
    font-weight: 700;
    font-size: 22px;
    letter-spacing: 2.6px;
    text-transform: uppercase;
    border-bottom: 2px solid var(--card-white);
  }

  .card-contact {
    flex: 1;
    background: var(--brand-blue);
    color: var(--text-light);
    padding: 30px 56px 0;
  }

  .contact-name {
    font-weight: 700;
    font-size: 40px;
    line-height: 1.1;
    margin-bottom: 14px;
  }

  .contact-list {
    list-style: none;
    font-size: 23px;
    line-height: 1.5;
    color: var(--text-soft);
  }

  .contact-label {
    font-style: italic;
  }
</style>
</head>
<body>
  <article class="business-card">
    <header class="card-brand">
      <span class="brand-name">Ridgeline Homes</span>
      <svg class="brand-mark" viewBox="0 0 56 56" aria-hidden="true">
        <circle cx="28" cy="28" r="24" fill="none" stroke="#1f3f86" stroke-width="5"/>
      </svg>
    </header>

    <div class="card-slogan">Setting the Standard for Community Living</div>

    <section class="card-contact">
      <h1 class="contact-name">Daniel Reyes</h1>
      <ul class="contact-list">
        <li><span class="contact-label">phone:</span> 555-014-2297</li>
        <li><span class="contact-label">web:</span> ridgelinehomes.example</li>
        <li><span class="contact-label">email:</span> dreyes@ridgelinehomes.example</li>
        <li><span class="contact-label">lic:</span> #RH 48 210</li>
        <li><span class="contact-label">address:</span> 410 Larkspur Avenue, Suite 12, Cedar Hollow, NY 12094</li>
      </ul>
    </section>
  </article>
</body>
</html>
```